Halvorsen Basin Holdings, LP Letter Head

We need an official company letter head design that is clean and mimics our company logo style. It will include our logo, address, phone, and website. We are an OIl and Gas mineral purchasing company, so hints of oil rigs or related design would be desirable.

Industry/Entity Type

Oil And Gas

Colors
ec1f27
f04a50
f59195
fbd4d5

Requirements
Must have
• Logo
• 7316 Marwick T. Ellsbury Parkway, Suite 418
• Dallas TX, 75391
• 214-763-1957
• www.halvorsenbasin.com
Nice to have
• Oil Rigs or OIl and gas related design

```html
<!DOCTYPE html>
<html lang="en">
<head>
<meta charset="utf-8">
<title>Halvorsen Basin Holdings, LP – Letterhead</title>
<link href="https://fonts.googleapis.com/css2?family=Cinzel:wght@400&family=Roboto:wght@400&display=swap" rel="stylesheet">
<style>
  :root {
    --backdrop: #3b3737;
    --paper: #f6f2f4;
    --brand-red: #b5121b;
    --brand-red-bright: #ec1f27;
    --watermark: #ebe1e6;
    --watermark-line: #f7f1f4;
    --ink: #2b2b2b;
    --rule: #9a9a9a;
  }
  * { box-sizing: border-box; margin: 0; padding: 0; }
  html, body {
    width: 1200px;
    height: 906px;
    overflow: hidden;
    background: var(--backdrop);
  }
  .letterhead {
    position: absolute;
    left: 296px;
    top: 23px;
    width: 608px;
    height: 860px;
    background: var(--paper);
    box-shadow: 0 6px 24px rgba(0,0,0,0.35);
  }
  .brand {
    position: absolute;
    top: 58px;
    left: 0;
    width: 100%;
    display: flex;
    flex-direction: column;
    align-items: center;
  }
  .brand-square {
    width: 62px;
    height: 62px;
    background: var(--brand-red);
    margin-bottom: 14px;
  }
  .brand-name {
    font-family: "Cinzel", serif;
    font-weight: 400;
    color: var(--brand-red);
    text-align: center;
    line-height: 1.25;
  }
  .brand-name .primary {
    display: block;
    font-size: 24px;
    letter-spacing: 1px;
  }
  .brand-name .secondary {
    display: block;
    font-size: 11px;
    letter-spacing: 5px;
  }
  .watermark {
    position: absolute;
    left: 164px;
    top: 300px;
    width: 280px;
    height: 280px;
    background: var(--watermark);
    outline: 10px solid var(--watermark-line);
    outline-offset: -22px;
  }
  .contact-strip {
    position: absolute;
    right: 36px;
    bottom: 34px;
    display: flex;
    align-items: center;
    gap: 12px;
    font-family: "Roboto", sans-serif;
    font-size: 9.5px;
    color: var(--ink);
    white-space: nowrap;
  }
  .contact-item {
    display: flex;
    align-items: center;
    gap: 5px;
  }
  .contact-icon {
    width: 10px;
    height: 10px;
    fill: none;
    stroke: var(--brand-red-bright);
    stroke-width: 1.4;
  }
  .contact-divider {
    width: 1px;
    height: 16px;
    background: var(--rule);
  }
</style>
</head>
<body>
  <main class="letterhead">
    <header class="brand">
      <div class="brand-square"></div>
      <div class="brand-name">
        <span class="primary">Halvorsen</span>
        <span class="secondary">Basin Holdings</span>
      </div>
    </header>

    <div class="watermark" role="img" aria-label="Faint brand square set as a background mark"></div>

    <footer class="contact-strip">
      <span class="contact-item">7316 Marwick T. Ellsbury Parkway, Suite 418, Dallas TX, 75391</span>
      <span class="contact-divider"></span>
      <span class="contact-item">
        <svg class="contact-icon" viewBox="0 0 10 10" aria-hidden="true">
          <path d="M2 1 L4 1 L4.6 3 L3.4 4 Q4.5 6 6 6.6 L7 5.4 L9 6 L9 8 Q5 9.5 1 4 Q1 2 2 1 Z"/>
        </svg>
        214-763-1957
      </span>
      <span class="contact-divider"></span>
      <span class="contact-item">
        <svg class="contact-icon" viewBox="0 0 10 10" aria-hidden="true">
          <rect x="0.8" y="2" width="8.4" height="6"/>
          <path d="M0.8 2 L5 5.4 L9.2 2"/>
        </svg>
        www.halvorsenbasin.com
      </span>
    </footer>
  </main>
</body>
</html>
```